Zia Bortolo's Crostoli

Looking for a packaging Label for Italian cookies. It has started with my great grandmothers Pizzelle recipe. Recipe has been in the family for over 100 years.
The packaging will be either clear plastic bags or Clear plastic hinged containers. Hoping for something elegant but traditional Italian. I have attached the company logo for color and idea possibilities
Would also like to give donation to helping animal foundations

Target Market(s)

Cookie lovers, coffee and tea drinkers, lighter alternative to heavy cookies

Requirements
Nice to have
• Family, Italian tradition

```html
<!DOCTYPE html>
<html lang="en">
<head>
<meta charset="utf-8">
<title>Zia Bortolo's Crostoli – Cookie Label</title>
<link rel="stylesheet" href="https://fonts.googleapis.com/css2?family=Rye&family=Oswald:wght@300;400&family=Libre+Baskerville:wght@400;700&family=Lato:wght@400&display=swap">
<style>
  :root {
    --backdrop: #bdbdbd;
    --label-cream: #f8dc9a;
    --pattern-tone: #fbe6b4;
    --brand-orange: #e9530f;
    --tab-white: #ffffff;
    --ink-dark: #231f1a;
  }
  html, body {
    margin: 0;
    padding: 0;
    width: 1200px;
    height: 861px;
    overflow: hidden;
    background: var(--backdrop);
  }
  .label-canvas {
    display: block;
    width: 1200px;
    height: 861px;
  }
  .label-base { fill: var(--label-cream); }
  .label-pattern { fill: url(#patternTone); }
  .label-ring { fill: none; stroke: var(--brand-orange); stroke-width: 3.5; }
  .brand-tab { fill: var(--tab-white); }
  .brand-name {
    font-family: "Libre Baskerville", serif;
    font-weight: 400;
    font-size: 30px;
    fill: var(--brand-orange);
  }
  .brand-tagline {
    font-family: "Lato", sans-serif;
    font-size: 15px;
    fill: var(--brand-orange);
  }
  .brand-dot { fill: var(--brand-orange); }
  .category-line {
    font-family: "Oswald", sans-serif;
    font-weight: 400;
    font-size: 27px;
    letter-spacing: 1px;
    fill: var(--ink-dark);
  }
  .flourish { fill: none; stroke: var(--ink-dark); stroke-width: 2; stroke-linecap: round; }
  .product-name {
    font-family: "Rye", serif;
    font-size: 92px;
    fill: var(--brand-orange);
  }
  .ribbon-band { fill: var(--brand-orange); }
  .ribbon-tail { fill: #c9440b; }
  .ribbon-edge { fill: none; stroke: var(--tab-white); stroke-width: 1.2; }
  .ribbon-text {
    font-family: "Libre Baskerville", serif;
    font-weight: 700;
    font-size: 15.5px;
    fill: var(--tab-white);
  }
  .net-weight {
    font-family: "Oswald", sans-serif;
    font-weight: 300;
    font-size: 25px;
    fill: var(--ink-dark);
  }
</style>
</head>
<body>
<svg class="label-canvas" viewBox="0 0 1200 861" xmlns="http://www.w3.org/2000/svg">
  <defs>
    <radialGradient id="patternTone" cx="50%" cy="50%" r="50%">
      <stop offset="0%" stop-color="#fae3ad"/>
      <stop offset="100%" stop-color="#f7d890"/>
    </radialGradient>
  </defs>

  <g class="round-label">
    <circle class="label-base" cx="600" cy="430" r="410"/>
    <circle class="label-pattern" cx="600" cy="430" r="410" role="img" aria-label="Cream ornamental damask pattern of swirls and flowers"/>
    <circle class="label-ring" cx="600" cy="430" r="393"/>

    <path class="brand-tab"
      d="M475 20 H721 V340
         l-8 8 l-8 -8 l-8 8 l-8 -8 l-8 8 l-8 -8 l-8 8 l-8 -8 l-8 8 l-8 -8 l-8 8 l-8 -8 l-8 8 l-8 -8
         l-8 8 l-8 -8 l-8 8 l-8 -8 l-8 8 l-8 -8 l-8 8 l-8 -8 l-8 8 l-8 -8 l-8 8 l-8 -8 l-8 8 l-8 -8
         l-8 8 l-8 -8 Z"/>

    <g class="brand-mark">
      <circle class="brand-dot" cx="598" cy="170" r="7"/>
      <text class="brand-name" x="598" y="232" text-anchor="middle">Zia Bortolo's</text>
      <text class="brand-tagline" x="598" y="290" text-anchor="middle">Italian Tradition</text>
    </g>

    <g class="category">
      <path class="flourish" d="M352 442 q12 -5 24 0 t24 0 M426 442 h-26"/>
      <path class="flourish" d="M848 442 q-12 -5 -24 0 t-24 0 M774 442 h26"/>
      <text class="category-line" x="600" y="452" text-anchor="middle">TRADITIONAL ITALIAN COOKIES</text>
    </g>

    <text class="product-name" x="600" y="572" text-anchor="middle" textLength="600" lengthAdjust="spacingAndGlyphs">CROSTOLI</text>

    <g class="ribbon">
      <path class="ribbon-tail" d="M368 622 H420 V670 H368 L384 646 Z"/>
      <path class="ribbon-tail" d="M832 622 H780 V670 H832 L816 646 Z"/>
      <rect class="ribbon-band" x="409" y="611" width="382" height="48"/>
      <rect class="ribbon-edge" x="413" y="615" width="374" height="40"/>
      <text class="ribbon-text" x="600" y="641" text-anchor="middle">FAMILY RECIPE FOR OVER 100 YEARS</text>
    </g>

    <text class="net-weight" x="600" y="762" text-anchor="middle">NET WT 10 oz (283 g)</text>
  </g>
</svg>
</body>
</html>
```